3 JPG Website Page Mockups need tidying / made into layered PSDs

Our website is aimed at creating a financial eduction site for females.

We have mockups of each page which are provided in jpeg.... but they need to be tidied up, layered into PSD (with descriptive layer names to allow coding from and no flattening - each object needs it's own layer) and we welcome any creative improvements suggested (although we are pretty happy with the way it's laid out at the moment as it is), without changing the feel, colour scheme or functionality of the site.

Three pages are needed:
Home page when not logged in
Home page when logged in
Topic header page

Please just upload the homepage to bid for the job... the winning designer will then have 5 days after they've been chosen to supply the psds of the other 2 pages .

I have also uploaded an image that can be used as a placeholder in the top box.
Thanks

As requested... Current font is Gill Sans MT

Thanks

Hi
Thanks for your designs.... For those of you still using the 4 circles (which I quite like), but haven't yet done so, could you see if you can move them around slightly to that the words don't get covered by the next circle?

Thanks

Reason: Designe has asked for An extension to work on new icons... would like to give them the time to see what they come up with, thanks

Industry/Entity Type

Financial

Requirements
Must have
• Maintain current feel & colour scheme of the website

```html
<!DOCTYPE html>
<html lang="en">
<head>
<meta charset="utf-8">
<title>Purse &amp; Purpose — Home</title>
<link rel="stylesheet" href="https://fonts.googleapis.com/css2?family=Noto+Serif:wght@400;700&family=Arimo:wght@400;700&display=swap">
<style>
:root{
  --navy:#063a5e;
  --navy-dark:#042c49;
  --orange:#f07d28;
  --grey-bg:#ececec;
  --grey-text:#8a8a8a;
  --body-text:#777;
  --border:#d6d6d6;
  --white:#fff;
  --tab-text:#9a9a9a;
}
*{box-sizing:border-box;margin:0;padding:0}
html,body{width:1197px;height:1200px;overflow:hidden;background:var(--white)}
body{font-family:"Noto Serif",serif;color:var(--navy);position:relative}
.abs{position:absolute}
.top-band{left:0;top:0;width:1197px;height:284px;background:var(--grey-bg)}
.home-tab{left:170px;top:32px;width:41px;height:32px;background:var(--navy);border-radius:5px 5px 0 0;display:flex;align-items:center;justify-content:center}
.main-nav{left:226px;top:36px;display:flex;font-size:18px;color:var(--tab-text)}
.main-nav span{padding:0 13px;border-left:2px dotted #bbb;line-height:20px}
.main-nav span:first-child{border-left:0;padding-left:0}
.header{left:170px;top:63px;width:857px;height:141px;background:var(--navy);border-radius:0 5px 0 0}
.logo{left:202px;top:84px;font-size:38px;line-height:34px;color:var(--white)}
.divider{width:0;border-left:2px dotted #5c7f99}
.search-label{left:403px;top:76px;font-size:14px;color:var(--white)}
.search-box{left:402px;top:100px;width:361px;height:26px;background:var(--white);border-radius:3px;font-family:Arimo,sans-serif;font-size:13px;color:#aaa;padding:5px 8px}
.search-box svg{position:absolute;right:10px;top:5px}
.sub-links{top:134px;font-size:13px;color:var(--white);text-align:center;white-space:nowrap}
.sub-links i{display:block;font-style:normal;font-size:9px;line-height:10px;color:#9bb}
.btn-light{top:108px;height:23px;background:linear-gradient(#fff,#e4e4e4);border:1px solid #b8c4cf;border-radius:3px;font-size:13px;color:var(--navy);padding:3px 7px;white-space:nowrap}
.welcome-bar{left:179px;top:177px;width:838px;height:27px;background:var(--white);display:flex;align-items:center;padding:0 10px;font-size:16px;color:#222;white-space:nowrap}
.welcome-bar b{color:#111}
.member{margin-left:auto;font-family:Arimo,sans-serif;font-size:12px;color:#222;display:flex;gap:10px;align-items:center}
.member strong{display:flex;align-items:center;gap:4px;margin-left:18px}
.sq{width:14px;height:14px;background:var(--orange);display:inline-block}
.hero{left:170px;top:203px;width:857px;height:268px;background:var(--white);border:1px solid var(--border);border-top:0;border-radius:0 0 5px 5px;overflow:hidden}
.hero-visual{left:355px;top:0;width:502px;height:268px;background:radial-gradient(circle at 30% 40%,#f4f6f8 0,#dfe6ec 45%,#bcd6e6 75%,#e9f1f6 100%)}
.hero-title{left:244px;top:270px;font-size:26px;line-height:28px;color:#111;white-space:nowrap}
.hero-title em{font-style:normal;color:var(--orange)}
.btn-navy{height:30px;background:linear-gradient(#1a5a86,var(--navy-dark));border-radius:4px;color:var(--white);font-size:14px;padding:5px 11px;box-shadow:0 2px 2px rgba(0,0,0,.3);white-space:nowrap}
.dot{top:434px;width:13px;height:13px;border-radius:50%;border:1px solid #bbb;background:var(--white)}
.dot.on{background:var(--navy);box-shadow:0 0 0 2px #fff,0 0 0 3px #bbb}
.panel{border:1px solid var(--border);border-radius:5px;background:var(--white)}
.video{left:200px;top:511px;width:309px;height:234px;border:2px solid #111;background:#222}
.video-frame{position:absolute;left:0;top:0;width:305px;height:212px;background:linear-gradient(135deg,#e8d6cf,#c9c7c4 50%,#7f8488)}
.video-bar{position:absolute;left:0;bottom:0;width:305px;height:18px;background:#111}
.topic{left:536px;top:516px;font-size:26px;line-height:28px;white-space:nowrap}
.topic span{color:#9a9a9a;font-weight:700;display:block}
.steps{width:326px;height:173px;background:linear-gradient(160deg,#fff 0,#eef4f8 50%,#d3e6f2 100%)}
.step-label{font-size:12px;font-weight:700;line-height:13px;text-align:center;color:var(--navy);white-space:nowrap}
.box-title{font-size:21px;color:var(--navy);white-space:nowrap}
.body-copy{font-family:Arimo,sans-serif;font-size:12px;line-height:14.7px;color:var(--body-text)}
.articles{left:624px;top:846px;list-style:none;font-family:Arimo,sans-serif;font-size:12.5px;color:var(--grey-text)}
.articles li{display:flex;align-items:center;gap:10px;height:29.5px;white-space:nowrap}
.shortcut{top:1035px;text-align:center;font-size:15px;width:140px;margin-left:-70px;white-space:nowrap}
.shortcut .icon{width:50px;height:50px;margin:0 auto 14px;border-radius:8px;background:linear-gradient(#e6e9ec,#b9c2ca)}
.footer-line{left:170px;top:1134px;width:857px;height:1px;background:var(--navy)}
.footer{top:1144px;font-family:Arimo,sans-serif;font-size:12.5px;color:var(--navy);white-space:nowrap}
</style>
</head>
<body>
<div class="abs top-band"></div>

<div class="abs home-tab"><svg width="22" height="18" viewBox="0 0 22 18"><path d="M11 1 1 9h3v8h5v-5h4v5h5V9h3z" fill="#fff"/></svg></div>
<nav class="abs main-nav"><span>Polls</span><span>Events</span><span>Learning Centre</span><span>Find an Adviser</span><span>Ask a Question</span><span>About us</span></nav>

<header class="abs header"></header>
<div class="abs logo">Purse<br>&amp;Purpose</div>
<div class="abs divider" style="left:388px;top:90px;height:60px"></div>
<div class="abs search-label">What are you looking for?</div>
<div class="abs search-box">Search Purse &amp; Purpose for...
  <svg width="18" height="16" viewBox="0 0 18 16"><circle cx="7" cy="6" r="5" fill="none" stroke="#888" stroke-width="2"/><path d="M11 9l6 6" stroke="#888" stroke-width="3"/></svg></div>
<div class="abs sub-links" style="left:404px">Popular<i>▾</i></div>
<div class="abs sub-links" style="left:479px">Explore the Learning Centre<i>▾</i></div>
<div class="abs sub-links" style="left:669px">Ask a Question<i>▾</i></div>
<div class="abs divider" style="left:781px;top:90px;height:60px"></div>
<div class="abs btn-light" style="left:798px">» Find an Advise</div>
<div class="abs btn-light" style="left:918px">» Contact us</div>

<div class="abs welcome-bar">Welcome to the new&nbsp;<b>Purse&amp;Purpose.</b>
  <div class="member">Already a member?<strong><i class="sq"></i>Login</strong><strong><i class="sq"></i>Forgotten Password</strong></div></div>

<section class="abs hero">
  <div class="abs hero-visual" role="img" aria-label="Stopwatch resting on a rising blue line chart"></div>
</section>
<svg class="abs" style="left:188px;top:312px" width="16" height="24" viewBox="0 0 16 24"><path d="M13 2 3 12l10 10" fill="none" stroke="#063a5e" stroke-width="4"/></svg>
<svg class="abs" style="left:993px;top:312px" width="16" height="24" viewBox="0 0 16 24"><path d="M3 2l10 10L3 22" fill="none" stroke="#063a5e" stroke-width="4"/></svg>
<h1 class="abs hero-title" style="font-weight:400">We’re Building World biggest<br>community Dedicated to the<br><em>Purse&amp;Purpose</em> of Women.</h1>
<div class="abs btn-navy" style="left:243px;top:373px">» join now for FREE</div>
<div class="abs dot" style="left:245px"></div>
<div class="abs dot on" style="left:264px"></div>
<div class="abs dot" style="left:283px"></div>

<section class="abs panel" style="left:170px;top:481px;width:857px;height:294px;overflow:hidden">
  <div class="abs steps" style="left:530px;top:119px" role="img" aria-label="People climbing a rising line of steps on a grid"></div>
</section>
<div class="abs video" role="img" aria-label="Video of two advisers with a client at a laptop">
  <div class="video-frame"></div>
  <svg style="position:absolute;left:124px;top:66px" width="60" height="84" viewBox="0 0 60 84"><path d="M0 0l60 42L0 84z" fill="#111"/></svg>
  <div class="video-bar"></div>
</div>
<h2 class="abs topic" style="font-weight:400">July Topic : Preparing for Retirement<span>Tomorrow Can Belong to Those<br>Whos Prepare Today.</span></h2>
<div class="abs btn-navy" style="left:536px;top:638px">» learn more</div>
<div class="abs step-label" style="left:724px;top:611px">5 Minute<br>Guide<br>PDF</div>
<div class="abs step-label" style="left:773px;top:677px">Take Our Poll<br>Vote</div>
<div class="abs step-label" style="left:880px;top:719px">Real Women<br>Real Storis<br>See Video</div>

<section class="abs panel" style="left:170px;top:784px;width:423px;height:224px"></section>
<h3 class="abs box-title" style="left:187px;top:802px;font-weight:400">Catch up with our latest Newsletter</h3>
<p class="abs body-copy" style="left:188px;top:839px;width:370px">Lorem Ipsum is simply dummy text of the printing and typesetting industry. Lorem Ipsum has been the industry's standard dummy text ever since the 1500s, when an unknown printer took a galley of type and scrambled it to make a type specimen book. It has survived not only five centuries, but also the leap into electronic typesetting, remaining essentially unchanged.</p>
<div class="abs" style="left:188px;top:962px;font-size:14px;white-space:nowrap">» See the Newsletter NOW</div>

<section class="abs panel" style="left:605px;top:784px;width:422px;height:224px"></section>
<h3 class="abs box-title" style="left:624px;top:802px;font-weight:400">Latest Articles of Interest</h3>
<ul class="abs articles">
  <li><svg width="20" height="18" viewBox="0 0 20 18"><path d="M10 1 1 9h3v8h12V9h3z" fill="#c9572c"/></svg>What is the real cost of having a bady</li>
  <li><svg width="20" height="18" viewBox="0 0 20 18"><path d="M1 16 7 9l4 4 8-11" fill="none" stroke="#d33" stroke-width="2"/></svg>Understanding the Risk and Returm of different asset types</li>
  <li><svg width="20" height="18" viewBox="0 0 20 18"><circle cx="9" cy="9" r="7" fill="none" stroke="#4a8bc2" stroke-width="2"/><path d="M9 5v4h3" stroke="#4a8bc2" stroke-width="2" fill="none"/></svg>How much do I need to Retire?</li>
  <li><svg width="20" height="18" viewBox="0 0 20 18"><path d="M1 16 7 9l4 4 8-11" fill="none" stroke="#d33" stroke-width="2"/></svg>Interest Rates and you</li>
</ul>

<div class="abs shortcut" style="left:236px"><div class="icon" role="img" aria-label="Shirt and tie icon"></div>Welcome</div>
<div class="abs shortcut" style="left:318px"><div class="icon" role="img" aria-label="Calendar icon"></div>Events</div>
<div class="abs shortcut" style="left:400px"><div class="icon" role="img" aria-label="Film reel icon"></div>Webcasts</div>
<div class="abs shortcut" style="left:494px"><div class="icon" role="img" aria-label="House icon"></div>My family</div>
<div class="abs shortcut" style="left:608px"><div class="icon" role="img" aria-label="Growth chart icon"></div>My Investments</div>
<div class="abs shortcut" style="left:739px"><div class="icon" role="img" aria-label="Clock and calendar icon"></div>My Retirement</div>
<div class="abs shortcut" style="left:850px"><div class="icon" role="img" aria-label="Handshake icon"></div>My Estate</div>
<div class="abs shortcut" style="left:950px"><div class="icon" style="border-radius:50%;background:radial-gradient(#6fcf4f,#2f9a27)" role="img" aria-label="Meditation icon"></div>My lifestyes</div>

<div class="abs footer-line"></div>
<div class="abs footer" style="left:179px">Copyright © 2000-2013 Purse &amp; Purpose.</div>
<div class="abs footer" style="left:918px">All rights reserved.</div>
</body>
</html>
```